Young Discovery Rooms Branding for Foundations
Young Discovery Rooms
ICON clarification
-How stuff works icon should show gears or the insides of a machine or electronic devise- not a lightbulb or question mark
- Physiology and food for thought icon should represent how the body functions and how food assists these functions. Perhaps you have an idea that shows a human silhouette with the esophagus or lungs highlighted? How about a bite out of food?
PLEASE PLEASE PLEASE refer to http://lomirvatel.example.com/ydr-branding-images-for-pelvox/
There is a LARGE CHANCE we will be choosing a design that is more of a GRAPHIC ORGANIZER (with littleto no illustrative components and more of our foundations listed with shapes and lines to show how they are connected) rather than a illustrative image that cannot be separated.
Please try a few versions of a graphic organizers shown on the above website.
Here are your perimeters;
-Use the 5-6 block graphic organizer as a start. Experiment with color and abbreviations and font and how icons can be incorporated into a graphic organizer that uses these rounded squares.
-Use the arrows in a circle as a basis for another idea/version. Experiment with color and abbreviations and font and how icons can be incorporated into a graphic organizer that uses a circular structure. (Be careful with arrows though, we don't want our image to insinuate any sort of progression or order.)
Designers: The contest has been extended 3 days! We will be contacting those designers who have ideas that we like- we want to give you feedback on some more simplified imagery.
To all designers, we would like you to check out http://lomirvatel.example.com/ydr-branding-images-for-pelvox/
and come up with a version of our five foundations that look like those featured on the above website. For instance, what can you do creatively that resembles the graphic organization of the circle with arrows? What can you do creatively that resembles the graphic organization of 5 squares? Think more graphic organizer than illustration for these- the more simple, the better.
On that website, we've also featured some ideas for icons to use for the Physiology and Food for Thought foundation. Physiology is anything having to do with how the body functions and food for thought represents how food helps these functions. Got ideas? Submit them!
Draft #50- great work! I like the drawings and the chalkboard without the word foundations. I also like addition of chalk sticks. Can I see this version with color or in bullets like the previous versions? Keep up the great work! More feedback soon...
Draft #56-58, Like the signs! The ladder version, #58 is interesting too. I like how you've taken the font of our logo and placed it on top, without the splash. More feedback soon...
Designers,
Keep up the great work. Our top ideas are the chalkboard, signs, and tree imagery. #42 is looking good and we like the icons chosen for both #42 and #44. Keep the ideas coming!
Really liking the sign ideas as in draft #33, 34, and 35!
Keep them coming!
We like #27 and #27 because they show our 5 foundations clear and in a sign format? Do you have more ideas? Keep them coming!
We also like draft #31, a chalkboard drawing. Any more ideas about that? The chalk drawings are good, but we would like to see the titles of our foundations separated, with bullets or icons. The chalkboard idea will work well with our website listing of our foundations, but the words and design on the board need to be able to stand alone for our other publications.
Keep showing us your best ideas!
Hey, LOOK AT LINK below, we put up examples of our own images that if you improve, you can win the contest. These are examples of simplicity!
http://lomirvatel.example.com/ydr-branding-images-for-pelvox/
Designers: NEW NEW NEW ideas! PLEASE READ!
After much thought, we decided that the YDR logo does not need to be in the design about the 5 foundations.... so, please dive deep into your creative brains and see if you can devise a design the solely focuses on the 5 foundations! Can't wait to see what you design!
Draft# 19 We are attracted to this because our logo is off center and not the center of attention. It has a clear background with an idea that links the foundations together. We LOVE the simplicity. However, the message says art, which we are not, so make sure the message adheres with our science center.
Got any ideas to use chalkboard drawings for our foundations?
How about posted signs like in draft #9?
We are looking for a quick visual that puts our 5 foundation titles together with simple shapes and colors.
Keep the designs coming and keep up the good work!
If anyone wants to experiment with solely using the 5 foundations and not the YDR logo, we are game for some options. We'd love to see if this enables more design ideas.
Similarly, if anyone wants to try adding a 6th Foundation, called Brightpath Craft Lab we are open to the options that might surface with having 6 foundations.
Keep up the good work!
As for Feedback:
Draft #21- I appreciate how different this design is! Can the apple and paintbrush be omitted or at least faded so they are not a visual focus? Also, can the colors be altered slightly to match those similar to the greens and oranges in our original logo. They are quite similar, but can they be made brighter?
Draft #22- Can I see what all the splash foundations look like as either puddles or with less splashes?
Thanks to all who are experimenting with new ideas and fonts. Keep them coming!
Draft #20- Thank you for your submission! We have tried images that deal with 6 and have found them to not work. I find the hands distracting because they are such as stark contrast to the design, logo and font.
Do you have any more ideas that show 5?
Thanks for the new design.
Draft #19 is god concept for our creativity and design foundation, however its to specific to that.
We would like to see a design that represents all of our 5 foundations. Thanks for more ideas!
Hello Designers. I've had a chance to think about the designs so far and don't think the hand imagery will work at all. There is a chance that we might invite older students to our center and a hand print is too elementary looking.
We are essentially asking you to create a design that organizes our 5 foundations in a creative way that is simple and clean but also complements the logo we already have.
Please do not change our logo or the way in which YDR could be abbreviated- I'm not a fan of collegiate lettering to abbreviate YDR.
We already have a cartoon-y tumbleworth style logo, so we are looking for our foundations to be cleaner, more graphic looking, rather than cartoon or childlike. However, the design needs to be kid friendly.
We have been attracted to white icon imagery placed on rounded squares in the past. Similar to Quince's marketing and application look. I've even thought about something that looks like a game of memory.
Please try different fonts. I'm not sure I like any that have been used so far.
I do not like the revision made to draft 18. The molecule sticks work better.

```html
<!DOCTYPE html>
<html lang="en">
<head>
<meta charset="utf-8">
<title>Young Discovery Rooms – Five Foundations Chalkboard Sign</title>
<link rel="stylesheet" href="https://fonts.googleapis.com/css2?family=Schoolbell&display=swap">
<style>
  :root {
    --page-bg: #ffffff;
    --page-shade: #f1f1f1;
    --cord: #4a4a4a;
    --nail: #2f2f2f;
    --outer-frame: #7f9468;
    --outer-frame-edge: #6b7f56;
    --wood-dark: #7a3d12;
    --wood-mid: #a85a1f;
    --wood-light: #c9792d;
    --board-dark: #141414;
    --board-mid: #2a2a28;
    --chalk-white: #e8e8e2;
    --chalk-blue: #9fd8e6;
    --chalk-yellow: #f3e74a;
    --chalk-red: #ef5a3a;
    --chalk-pink: #f06fa8;
    --chalk-lime: #e9f07a;
    --chalk-orange: #f5a623;
    --chalk-green: #8cc63f;
  }
  * { box-sizing: border-box; margin: 0; padding: 0; }
  html, body {
    width: 1200px;
    height: 1016px;
    overflow: hidden;
  }
  body {
    background: radial-gradient(ellipse at 50% 45%, var(--page-bg) 55%, var(--page-shade) 100%);
    position: relative;
    font-family: "Schoolbell", cursive;
  }
  .sign-art {
    position: absolute;
    inset: 0;
    width: 1200px;
    height: 1016px;
  }
  .foundations {
    position: absolute;
    left: 220px;
    top: 292px;
    width: 751px;
    height: 498px;
    list-style: none;
  }
  .foundation {
    position: absolute;
    left: 0;
    width: 100%;
    text-align: center;
    font-size: 36px;
    line-height: 40px;
    letter-spacing: 0.5px;
    white-space: nowrap;
  }
  .foundation--physiology { top: 95px; color: var(--chalk-blue); }
  .foundation--science { top: 161px; color: var(--chalk-yellow); }
  .foundation--science .accent { color: var(--chalk-red); }
  .foundation--stuff { top: 230px; color: var(--chalk-pink); }
  .foundation--creativity { top: 299px; color: var(--chalk-lime); }
  .foundation--planet { top: 368px; color: var(--chalk-orange); }
  .chalk-mark {
    position: absolute;
    font-size: 46px;
    line-height: 1;
    color: var(--chalk-white);
    left: 940px;
    top: 352px;
  }
</style>
</head>
<body>
  <svg class="sign-art" viewBox="0 0 1200 1016" xmlns="http://www.w3.org/2000/svg">
    <defs>
      <linearGradient id="wood-grain" x1="0" y1="0" x2="1" y2="1">
        <stop offset="0" stop-color="#c9792d"/>
        <stop offset="0.5" stop-color="#a85a1f"/>
        <stop offset="1" stop-color="#7a3d12"/>
      </linearGradient>
      <radialGradient id="board-surface" cx="0.5" cy="0.45" r="0.7">
        <stop offset="0" stop-color="#2a2a28"/>
        <stop offset="1" stop-color="#141414"/>
      </radialGradient>
    </defs>

    <g class="hanging-cord" stroke="var(--cord)" stroke-width="4" fill="none">
      <line x1="600" y1="77" x2="455" y2="238"/>
      <line x1="600" y1="77" x2="748" y2="238"/>
    </g>
    <circle class="nail" cx="600" cy="77" r="8" fill="var(--nail)"/>

    <rect class="outer-frame" x="157" y="228" width="881" height="625" rx="30"
          fill="var(--outer-frame)" stroke="var(--outer-frame-edge)" stroke-width="3"/>
    <rect class="wood-frame" x="182" y="253" width="828" height="573" rx="8" fill="url(#wood-grain)"/>
    <g class="wood-corners" stroke="var(--wood-dark)" stroke-width="2" opacity="0.6">
      <line x1="182" y1="253" x2="220" y2="292"/>
      <line x1="1010" y1="253" x2="971" y2="292"/>
      <line x1="182" y1="826" x2="220" y2="790"/>
      <line x1="1010" y1="826" x2="971" y2="790"/>
    </g>
    <rect class="chalkboard" x="220" y="292" width="751" height="498" fill="url(#board-surface)"/>

    <path class="chalk-loop" fill="none" stroke="var(--chalk-white)" stroke-width="3"
          stroke-dasharray="12 10" stroke-linecap="round"
          d="M330 326 C 500 316, 700 328, 800 320 C 880 314, 928 370, 926 450
             C 924 540, 938 620, 908 700 C 890 742, 840 750, 760 750
             L 420 752 C 320 754, 268 742, 266 702 C 264 650, 298 600, 284 540
             C 270 480, 258 420, 288 368 C 298 344, 310 328, 330 326 Z"/>

    <circle role="img" aria-label="Chalk atom icon" cx="850" cy="356" r="16" fill="var(--chalk-white)" opacity="0.35"/>
    <rect role="img" aria-label="Chalk lab flask icon" x="302" y="436" width="44" height="50" rx="8" fill="var(--chalk-blue)" opacity="0.4"/>
    <circle role="img" aria-label="Chalk globe icon" cx="872" cy="495" r="28" fill="var(--chalk-green)" opacity="0.45"/>
    <rect role="img" aria-label="Chalk magnet icon" x="362" y="520" width="40" height="36" rx="10" fill="var(--chalk-white)" opacity="0.35"/>
    <rect role="img" aria-label="Chalk rocket icon" x="800" y="556" width="34" height="38" rx="12" fill="var(--chalk-white)" opacity="0.35"/>
    <rect role="img" aria-label="Chalk pencil icon" x="318" y="594" width="64" height="24" rx="6" fill="var(--chalk-yellow)" opacity="0.35"/>
    <rect role="img" aria-label="Chalk leaf icon" x="630" y="643" width="22" height="12" rx="6" fill="var(--chalk-green)" opacity="0.55"/>
  </svg>

  <span class="chalk-mark" aria-hidden="true">?</span>

  <ul class="foundations">
    <li class="foundation foundation--physiology">Physiology n Food for Thought</li>
    <li class="foundation foundation--science">Science <span class="accent">FUN</span>damentals</li>
    <li class="foundation foundation--stuff">How Stuff Works</li>
    <li class="foundation foundation--creativity">Creativity n Design</li>
    <li class="foundation foundation--planet">Planet Earth n Green Technology</li>
  </ul>
</body>
</html>
```